Layla Karim Haddad Desert Fragrances

All our perfumes are non-alcoholic and water based. We want to have a design that would have some Arabic calligraphy, arabesque etc. We would be the label theme u design for all our scents. Of course, the scent flavor would changed. We will also use the pattern on the packaging of the scent as well. Something along the lines of this brand: http://veridocrest.example/en/.
Label size: Length 6"; Height 5"

Target Market(s)

middle east (Kuwait, UAE, Saudi Arabia);

Requirements
Must have
• 1. Flavor Name (editable)
• 2. Quantity 240 ml / 100 ml (editable)
• 3. Flavor Description (editable. each flavor has its own unique description)
• 4. Logo (place where we can display our logo. Logo file submitted.)
• 5. Company Name (editable. I should be able to edit this field too.)
Nice to have
• Flavor name in English and Arabic. You don't have to do any translation. Just make a space for us so that we can type-in the Arabic name. It wud be good to place the Arabic flavor name right below the English one.
Should not have
• images of animals, people

```html
<!DOCTYPE html>
<html lang="en">
<head>
<meta charset="utf-8">
<title>Layla Karim Haddad Desert Fragrances – Perfume Label</title>
<link rel="stylesheet" href="https://fonts.googleapis.com/css2?family=Great+Vibes&family=Tangerine:wght@400;700&family=Reem+Kufi:wght@500&display=swap">
<style>
  :root {
    --paper: #ffffff;
    --ink: #3e302b;
    --ink-soft: #7d6f6a;
    --bronze: #8a5a2b;
    --bronze-light: #c79a63;
    --seal-line: #8d8582;
  }
  * { margin: 0; padding: 0; box-sizing: border-box; }
  html, body { width: 1200px; height: 1000px; overflow: hidden; background: var(--paper); }
  .label {
    position: relative;
    width: 1200px;
    height: 1000px;
    background: var(--paper);
    color: var(--ink);
  }
  .corner-ornament {
    position: absolute;
    background: radial-gradient(circle at var(--origin), var(--bronze) 0%, var(--bronze-light) 45%, rgba(199,154,99,0) 75%);
    opacity: .85;
  }
  .corner-ornament--top-left { left: 0; top: 0; width: 220px; height: 175px; --origin: 0 0; }
  .corner-ornament--top-right { right: 0; top: 0; width: 220px; height: 175px; --origin: 100% 0; }
  .corner-ornament--bottom-left { left: 0; bottom: 0; width: 160px; height: 330px; --origin: 0 100%; }
  .corner-ornament--bottom-right { right: 0; bottom: 0; width: 160px; height: 330px; --origin: 100% 100%; }

  .logo-seal {
    position: absolute;
    left: 430px;
    top: 22px;
    width: 340px;
    height: 340px;
  }
  .logo-seal__name {
    font-family: 'Tangerine', cursive;
    font-weight: 700;
    font-size: 46px;
    fill: var(--ink);
  }

  .company-name {
    position: absolute;
    left: 0; right: 0;
    top: 420px;
    text-align: center;
    font-family: 'Great Vibes', cursive;
    font-size: 84px;
    line-height: 1;
    color: var(--ink);
  }

  .divider-ornament {
    position: absolute;
    left: 455px;
    width: 290px;
    background: linear-gradient(90deg, rgba(138,90,43,0) 0%, var(--bronze) 30%, var(--bronze) 70%, rgba(138,90,43,0) 100%);
    opacity: .8;
  }
  .divider-ornament--top { top: 540px; height: 85px; }
  .divider-ornament--bottom { top: 865px; height: 28px; left: 500px; width: 200px; }

  .flavor-name {
    position: absolute;
    left: 0; right: 0;
    top: 632px;
    text-align: center;
    font-family: 'Great Vibes', cursive;
    font-size: 50px;
    line-height: 1;
    color: var(--ink-soft);
  }
  .flavor-description {
    position: absolute;
    left: 0; right: 0;
    top: 690px;
    text-align: center;
    font-family: 'Great Vibes', cursive;
    font-size: 34px;
    line-height: 1;
    color: var(--ink);
  }
  .flavor-name-arabic,
  .flavor-description-arabic {
    position: absolute;
    left: 0; right: 0;
    text-align: center;
    font-family: 'Reem Kufi', sans-serif;
    font-weight: 500;
    line-height: 1;
    direction: rtl;
  }
  .flavor-name-arabic { top: 730px; font-size: 66px; color: var(--ink-soft); }
  .flavor-description-arabic { top: 800px; font-size: 60px; color: var(--ink); }

  .quantity {
    position: absolute;
    left: 185px;
    top: 955px;
    font-family: 'Great Vibes', cursive;
    font-size: 30px;
    line-height: 1;
    color: var(--ink);
  }
</style>
</head>
<body>
<main class="label">
  <div class="corner-ornament corner-ornament--top-left" role="img" aria-label="Arabesque floral scroll ornament in bronze"></div>
  <div class="corner-ornament corner-ornament--top-right" role="img" aria-label="Arabesque floral scroll ornament in bronze"></div>
  <div class="corner-ornament corner-ornament--bottom-left" role="img" aria-label="Arabesque floral scroll ornament in bronze"></div>
  <div class="corner-ornament corner-ornament--bottom-right" role="img" aria-label="Arabesque floral scroll ornament in bronze"></div>

  <svg class="logo-seal" viewBox="0 0 340 340" aria-label="Layla Karim Haddad">
    <circle cx="170" cy="170" r="162" fill="none" stroke="var(--seal-line)" stroke-width="4"/>
    <text class="logo-seal__name" x="170" y="164" text-anchor="middle">Layla Karim</text>
    <text class="logo-seal__name" x="170" y="206" text-anchor="middle">Haddad</text>
  </svg>

  <h1 class="company-name">Company Name</h1>

  <div class="divider-ornament divider-ornament--top" role="img" aria-label="Symmetrical arabesque flourish divider"></div>

  <p class="flavor-name">Flavor Name</p>
  <p class="flavor-description">Flavor Description</p>
  <p class="flavor-name-arabic" lang="ar">اسم العطر</p>
  <p class="flavor-description-arabic" lang="ar">وصف العطر</p>

  <div class="divider-ornament divider-ornament--bottom" role="img" aria-label="Small arabesque flourish"></div>

  <p class="quantity">Quantity 240 ml / 100 ml</p>
</main>
</body>
</html>
```